**Business Card**Designs Project** TorvaleHoldings,LLC

Im looking for a simple and elegant Business Card that has a professional Corporate look and feel. Im considering a Metal business card as well as 2 color layout, Embossed, 1 color two tone layout(File#6 like).

The card should NOT be too busy but subtle. Clean look providing Key Details.

please see uploaded files for actual logo and inspirational design i like.

See Uploaded File # 3 for Professional Logos Style

Target Market(s)

investors

Industry/Entity Type

Business

Contact Information for Business Card

Side 1 information
Torvale Holdings,LLC - Description Text below main logo = (Funding - Sales) or (Commercial - Residential) or (Property - Funding )
www.torvaleholdings.example

Side 2 Information =
Lem Korrin | Managing Broker
P 555-184-6072 | F 555-730-4158
E info@torvaleholdings.example
membership logos - see file #3 for stye and file #4 for inspiration

Side 2 = 10pt Font
BRE: 07261843
NMLS: 6827354

Colors
3277b5
5c5c5c
333333
959595
85acd3
1b1b1b
ffffff

Requirements
Must have
• Torvale Holdings, LLC **T Logo** - See Uploaded File #5 ,
• Contact Information - See Business Card Details Above
• Web address = www.torvaleholdings.example
• Membership logos - See Uploaded File #4 & 9
Nice to have
• 1 Color two tones, grey, White, Charcoal Grey, Dark Turquois, Dark blue, Slate blue,
• GOOD COMBINATIONS: White and Grey, white and Charcoal grey with a splash of blue, Charcoal grey card with White, etc..
• PLEASE TRY DARK BLUE DESIGNS
• Embossed, card designs
• Metal Business card design
Should not have
• I DONT LIKE ALOTE OF WAVE DESIGNS

```html
<!DOCTYPE html>
<html lang="en">
<head>
<meta charset="utf-8">
<title>Torvale Holdings, LLC — Business Card</title>
<link rel="stylesheet" href="https://fonts.googleapis.com/css2?family=Questrial&display=swap">
<style>
  :root {
    --brand-blue: #3277b5;
    --blue-tone: #2b6aa3;
    --light-blue: #85acd3;
    --slate: #5c5c5c;
    --charcoal: #333333;
    --mid-grey: #959595;
    --paper: #ffffff;
    --stage: #e4e4e4;
    --emboss-line: #e6e6e6;
  }
  * { margin: 0; padding: 0; box-sizing: border-box; }
  html, body { width: 1200px; height: 800px; overflow: hidden; }
  body {
    background: var(--stage);
    font-family: "Questrial", sans-serif;
    position: relative;
  }
  .card {
    position: absolute;
    top: 130px;
    width: 300px;
    height: 540px;
  }
  .card--front { left: 270px; background: var(--brand-blue); }
  .card--back { left: 630px; background: var(--paper); }

  .brand-ring {
    position: absolute;
    left: 75px;
    top: 60px;
    width: 150px;
    height: 150px;
    border-radius: 50%;
    border: 14px solid var(--blue-tone);
  }
  .card--back .brand-ring { border-color: var(--emboss-line); left: 100px; top: 50px; }

  .brand-name {
    position: absolute;
    left: 0; right: 0;
    top: 300px;
    text-align: center;
    color: var(--blue-tone);
    font-size: 27px;
    letter-spacing: 0.5px;
    line-height: 1.15;
  }
  .website {
    position: absolute;
    left: 0; right: 0;
    bottom: 52px;
    text-align: center;
    color: var(--paper);
    font-size: 17px;
    letter-spacing: 0.3px;
  }

  .contact {
    position: absolute;
    left: 32px;
    top: 238px;
    color: var(--slate);
    font-size: 15.5px;
    line-height: 1.45;
  }
  .contact__name { color: var(--brand-blue); font-size: 21px; font-weight: 400; letter-spacing: 0.5px; line-height: 1.2; }
  .contact__title { font-size: 16px; margin-bottom: 8px; }
  .contact__row { display: flex; align-items: center; gap: 5px; }
  .contact__row svg { width: 12px; height: 12px; flex: none; }
  .badges {
    position: absolute;
    left: 32px;
    top: 462px;
    display: flex;
    gap: 10px;
  }
  .badge { width: 34px; height: 38px; border: 3px solid var(--slate); }
</style>
</head>
<body>
  <section class="card card--front" aria-label="Card front">
    <div class="brand-ring"></div>
    <p class="brand-name">Torvale Holdings, LLC</p>
    <p class="website">www.torvaleholdings.example</p>
  </section>

  <section class="card card--back" aria-label="Card back">
    <div class="brand-ring"></div>
    <div class="contact">
      <h1 class="contact__name">Lem Korrin</h1>
      <p class="contact__title">Managing Broker</p>
      <p>BRE: 07261843</p>
      <p>NMLS: 6827354</p>
      <p class="contact__row">
        <svg viewBox="0 0 12 12" aria-hidden="true"><path d="M2 1l3 0 1 3-1.5 1a6 6 0 0 0 2.5 2.5L8 6l3 1v3a1 1 0 0 1-1 1A9 9 0 0 1 1 2a1 1 0 0 1 1-1z" fill="var(--brand-blue)"/></svg>
        555-184-6072
      </p>
      <p class="contact__row">
        <svg viewBox="0 0 12 12" aria-hidden="true"><rect x="3" y="1" width="6" height="3" fill="var(--brand-blue)"/><rect x="1" y="4.5" width="10" height="4.5" rx="1" fill="var(--brand-blue)"/><rect x="3" y="8" width="6" height="3" fill="var(--brand-blue)"/></svg>
        555-730-4158
      </p>
      <p class="contact__row">
        <svg viewBox="0 0 12 12" aria-hidden="true"><rect x="0.5" y="2" width="11" height="8" fill="var(--brand-blue)"/><path d="M0.5 2l5.5 4.5L11.5 2" fill="none" stroke="var(--paper)" stroke-width="1"/></svg>
        info@torvaleholdings.example
      </p>
    </div>
    <div class="badges" aria-label="Membership badges">
      <div class="badge"></div>
      <div class="badge"></div>
    </div>
  </section>
</body>
</html>
```